Stationery Design Project

We are looking for a full revision of our existing stationary to include within this project:

- Letterhead
- Business card
- Compliment slip

The items should be a reflection of our new website which can be found at http://www.brackenledger.co.uk/

Our logo files are included within the file brief

There are some further projects which we may approach the winning designer for as we need a revision to the front cover of our reports, a new price list and two brochures for specific target markets.

Industry/Entity Type

Business

```html
<!DOCTYPE html>
<html lang="en">
<head>
<meta charset="utf-8">
<title>Bracken Ledger Stationery</title>
<link href="https://fonts.googleapis.com/css2?family=PT+Sans&family=Source+Sans+3:wght@300;400;600&display=swap" rel="stylesheet">
<style>
:root{
  --backdrop:#c6c6c6;
  --paper:#ffffff;
  --navy:#1f1f6b;
  --blue:#2b63ad;
  --blue-deep:#243e96;
  --blue-light:#3a7fc0;
  --sky:#1a8ad0;
  --ink:#2a2a2a;
  --muted:#7a7a7a;
}
*{margin:0;padding:0;box-sizing:border-box}
html,body{width:1200px;height:900px;overflow:hidden;background:var(--backdrop)}
.canvas{position:relative;width:1200px;height:900px}
.sheet{position:absolute;background:var(--paper);overflow:hidden}
.wordmark{font-family:"Source Sans 3",sans-serif;font-weight:600;color:var(--navy);white-space:nowrap;letter-spacing:.2px}
.wave{position:absolute;left:0;bottom:0;display:block}

/* letterhead */
.letterhead{left:72px;top:53px;width:612px;height:792px}
.letterhead .wordmark{position:absolute;left:36px;top:56px;font-size:25px}
.letterhead .address{position:absolute;left:463px;top:48px;font-family:"Source Sans 3",sans-serif;font-weight:300;font-size:9.5px;line-height:12px;color:var(--muted)}
.label{color:var(--blue);font-weight:600}
.letter-body{position:absolute;left:93px;top:233px;width:446px;font-family:"PT Sans",sans-serif;font-size:9.3px;line-height:10.6px;color:var(--ink);text-align:justify}
.letter-body p{margin-bottom:10.6px}
.signature{position:absolute;left:100px;top:533px;width:100px;height:62px;background:#ececf0;border-radius:4px}
.letterhead .web{position:absolute;left:78px;bottom:6px;font-family:"Source Sans 3",sans-serif;font-size:9.5px;color:#fff}

/* business card */
.card-front{left:765px;top:89px;width:252px;height:144px;background:radial-gradient(circle at 40% 30%,var(--sky),#1a5ca8 55%,#1a4a92)}
.card-front .wordmark{position:absolute;left:118px;top:118px;font-size:13px;color:#fff}
.card-back{left:765px;top:239px;width:252px;height:143px}
.card-back .wordmark{position:absolute;left:12px;top:22px;font-size:13px}
.holder{position:absolute;left:27px;top:78px;font-family:"Source Sans 3",sans-serif}
.holder .name{font-size:9.5px;font-weight:600;color:var(--blue)}
.holder .role{font-size:6px;color:var(--muted)}
.divider{position:absolute;left:119px;top:58px;width:1px;height:40px;background:#c9c9c9}
.contact{position:absolute;left:142px;top:63px;font-family:"Source Sans 3",sans-serif;font-size:5.8px;line-height:8.3px;color:var(--muted);list-style:none}
.contact .icon{display:inline-block;width:4px;height:4px;border-radius:50%;background:var(--blue);margin-right:3px;vertical-align:middle}

/* compliment slip */
.comp-slip{left:516px;top:425px;width:632px;height:274px;box-shadow:0 1px 4px rgba(0,0,0,.25)}
.comp-slip .wordmark{position:absolute;left:30px;top:42px;font-size:19px}
.comp-slip .address{position:absolute;left:25px;top:75px;font-family:"Source Sans 3",sans-serif;font-weight:300;font-size:9.5px;line-height:12.5px;color:var(--muted)}
.compliments{position:absolute;left:347px;top:230px;font-family:"Source Sans 3",sans-serif;font-size:21px;color:var(--blue)}
</style>
</head>
<body>
<div class="canvas">

  <section class="sheet letterhead">
    <div class="wordmark">Bracken Ledger</div>
    <div class="address">
      418 Larkmoor Street<br>
      Suite 210 Halden, CA 94021<br>
      <span class="label">Phone.</span> (415) 555-0142<br>
      <span class="label">Fax.</span> (415) 555-0143
    </div>
    <div class="letter-body">
      <p>In dui turpis, varius vitae, tincidunt id, consequat ut, leo. Donec tincidunt tristique odio. Nulla erat felis, euismod nec, fringilla non, aliquet et, magna. Nulla at magna quis nisi pretium vehicula. Pellentesque habitant morbi tristique senectus et netus et malesuada fames ac turpis egestas. Class aptent taciti sociosqu ad litora torquent per conubia nostra, per inceptos himenaeos. In vel quam. Phasellus varius convallis purus. In non turpis. Nam sed risus. Etiam non neque at nisl gravida porttitor. Donec leo dolor, feugiat ut, pharetra et, porttitor a, metus. Suspendisse laoreet magna vel elit. Ut est augue, fermentum ac, molestie at, vestibulum et, urna.</p>
      <p>Nunc purus. Cras auctor. In ornare neque id ipsum. Nulla tincidunt, diam sit amet viverra euismod, sapien augue fringilla neque, at pellentesque felis tortor vel enim. Etiam dignissim. Sed a tortor vel nisl euismod ultricies. Donec molestie congue lectus. Integer sed turpis a tortor imperdiet consequat. Maecenas molestie placerat urna. Sed pede enim, sollicitudin nec, pretium nec, sollicitudin a, felis. In hac habitasse platea dictumst. Nam facilisis, tellus nec lacinia interdum, erat, turpis turpis semper ante, euismod imperdiet augue nisi et neque. Vivamus non metus.</p>
      <p>Nulla lobortis ultricies nulla. Pellentesque purus mi, consequat quis, hendrerit vitae, tincidunt non, eros. Nullam urna est, vehicula nec, cursus nec, dignissim sit amet, lectus. Nunc vel tellus sit amet laoreet ullamcorper, urna nisi fringilla ante, at rhoncus justo enim at turpis. Duis hendrerit luctus lorem. Aenean tempor, metus vel posuere gravida, arcu nunc fermentum magna, blandit sem magna a turpis. Vivamus in neque. Lorem ipsum dolor sit amet, consectetuer adipiscing elit. Duis tristique tortor id nisl feugiat posuere. Maecenas posuere hendrerit. Praesent porta tempus ligula. Morbi in leo. Curabitur sapien nulla, faucibus in, porttitor et, odio. Praesent sed justo sed arcu commodo feugiat. Duis tempor. Cras libero. Donec mollis consectetuer metus. Praesent odio.</p>
    </div>
    <div class="signature" role="img" aria-label="Handwritten signature"></div>
    <svg class="wave" width="612" height="80" viewBox="0 0 612 80" aria-hidden="true">
      <defs><linearGradient id="lhBand" x1="0" x2="1"><stop offset="0" stop-color="var(--blue-light)"/><stop offset="1" stop-color="var(--blue-deep)"/></linearGradient></defs>
      <path d="M0,42 Q90,8 150,14 Q260,30 330,62 Q470,72 612,18 L612,80 L0,80 Z" fill="url(#lhBand)"/>
    </svg>
    <div class="web">www.brackenledger.co.uk</div>
  </section>

  <section class="sheet card-front">
    <svg class="wave" width="252" height="40" viewBox="0 0 252 40" aria-hidden="true">
      <path d="M0,30 Q60,12 120,22 Q190,34 252,26" fill="none" stroke="rgba(255,255,255,.25)" stroke-width="1.2"/>
      <path d="M0,36 Q70,20 130,28 Q200,38 252,32" fill="none" stroke="rgba(255,255,255,.18)" stroke-width="1"/>
    </svg>
    <div class="wordmark">Bracken Ledger</div>
  </section>

  <section class="sheet card-back">
    <div class="wordmark">Bracken Ledger</div>
    <div class="holder">
      <div class="name">Mara Ellison</div>
      <div class="role">Managing Director</div>
    </div>
    <div class="divider"></div>
    <ul class="contact">
      <li>1290 Westfield Loop</li>
      <li>Ardmore, TX 78011</li>
      <li><span class="icon"></span>(415) 555-0142</li>
      <li><span class="icon"></span>(415) 555-0143</li>
      <li><span class="icon"></span>mara@brackenledger.co.uk</li>
      <li><span class="icon"></span>www.brackenledger.co.uk</li>
    </ul>
    <svg class="wave" width="252" height="30" viewBox="0 0 252 30" aria-hidden="true">
      <defs><linearGradient id="cardBand" x1="0" x2="1"><stop offset="0" stop-color="var(--blue-light)"/><stop offset="1" stop-color="var(--blue-deep)"/></linearGradient></defs>
      <path d="M0,16 Q35,4 60,6 Q100,14 130,26 Q190,30 252,8 L252,30 L0,30 Z" fill="url(#cardBand)"/>
    </svg>
  </section>

  <section class="sheet comp-slip">
    <div class="wordmark">Bracken Ledger</div>
    <div class="address">
      418 Larkmoor Street<br>
      Suite 210 Halden, CA 94021
    </div>
    <svg class="wave" width="632" height="70" viewBox="0 0 632 70" aria-hidden="true">
      <defs><linearGradient id="slipBand" x1="0" x2="1"><stop offset="0" stop-color="var(--blue-light)"/><stop offset="1" stop-color="var(--blue-deep)"/></linearGradient></defs>
      <path d="M0,38 Q90,8 135,4 Q230,30 300,60 Q480,64 632,18 L632,70 L0,70 Z" fill="url(#slipBand)"/>
    </svg>
    <div class="compliments">With Compliments</div>
  </section>

</div>
</body>
</html>
```